Hot young IT advisor needs business cards as upscale and innovative as they are

We need business cards that make a statement about who we are, as a young and upscale IT advisor. Our whole angle is innovation and tenacity in our personal relationships with our clients. We've just done a brand overhaul and need cards that have the new logos, but we're also looking for someone with a sixth sense who can capture what sets us apart and communicate that with a business card. Clean, minimalist, upscale, innovative, personal. Our budget only allows room for them to be soft-touch, no spot gloss or foil designs please.

Target Market(s)

High-level decision makers at middle-market and large organizations in the healthcare, financial services, sports and entertainment, K-12 education, college and university, state and local government, and federal government sectors.

Industry/Entity Type

Information Technology

Font styles to use
Sans Serif

Colors
ec1f27
606060
ffffff

Requirements
Should not have
• Designs with low contrast which would require spot-gloss or embossing.

```html
<!DOCTYPE html>
<html lang="en">
<head>
<meta charset="UTF-8">
<title>Kestran Business Cards</title>
<link href="https://fonts.googleapis.com/css2?family=Roboto+Condensed:wght@400;700&family=Montserrat:wght@400&display=swap" rel="stylesheet">
<style>
  :root {
    --brand-red: #ec1f27;
    --text-grey: #606060;
    --paper: #ffffff;
    --card-dark: #2b2a2a;
    --pattern-tone: #3a3939;
    --backdrop: #e4e5e7;
  }
  * { margin: 0; padding: 0; box-sizing: border-box; }
  html, body {
    width: 1200px; height: 800px; overflow: hidden;
    background: var(--backdrop);
    font-family: "Roboto Condensed", "Arial Narrow", sans-serif;
  }
  .canvas { position: relative; width: 1200px; height: 800px; }

  .card {
    position: absolute;
    width: 560px; height: 320px;
    box-shadow: 0 6px 18px rgba(0,0,0,0.18);
  }

  /* Back face */
  .card-back { left: 360px; top: 50px; background: var(--card-dark); overflow: hidden; }
  .card-back .pattern-fill {
    position: absolute; inset: 0;
    background: linear-gradient(135deg, var(--card-dark) 0%, var(--pattern-tone) 50%, var(--card-dark) 100%);
  }
  .card-back .wordmark {
    position: absolute; inset: 0;
    display: flex; align-items: center; justify-content: center;
    font-family: "Montserrat", sans-serif;
    font-weight: 400; font-size: 34px; letter-spacing: 0.32em;
    color: var(--paper);
    padding-left: 0.32em;
  }

  /* Front face */
  .card-front { left: 240px; top: 430px; background: var(--paper); }
  .brand {
    position: absolute; left: 70px; top: 140px;
    display: flex; align-items: center; gap: 10px;
  }
  .brand-square { width: 22px; height: 22px; background: var(--brand-red); }
  .brand-name {
    font-weight: 700; font-size: 26px; letter-spacing: 0.04em;
    color: var(--brand-red);
  }

  .details {
    position: absolute; left: 270px; bottom: 40px;
    display: flex; align-items: flex-end; gap: 26px;
  }
  .column {
    writing-mode: vertical-rl;
    transform: rotate(180deg);
    font-size: 15px; line-height: 1.15;
    color: var(--text-grey);
  }
  .person-name {
    font-weight: 700; font-size: 20px; color: var(--brand-red);
    letter-spacing: 0.02em;
  }
  .person-title { font-size: 16px; }
  .contact-line { display: flex; align-items: center; gap: 6px; }
  .contact-line svg { width: 11px; height: 11px; transform: rotate(90deg); }
  .accent { color: var(--brand-red); }
</style>
</head>
<body>
<main class="canvas">

  <section class="card card-back">
    <div class="pattern-fill" role="img" aria-label="Dark repeating brand pattern background"></div>
    <div class="wordmark">KESTRAN</div>
  </section>

  <section class="card card-front">
    <div class="brand">
      <span class="brand-square"></span>
      <span class="brand-name">KESTRAN</span>
    </div>

    <div class="details">
      <div class="column identity">
        <div class="person-name">DANA WHITFIELD</div>
        <div class="person-title">President/CEO</div>
      </div>
      <div class="column address">
        <div>410 Harbor Ave Suite 220</div>
        <div>Buffalo, NY 14203</div>
      </div>
      <div class="column contact">
        <div class="contact-line">
          <svg viewBox="0 0 12 12" aria-hidden="true"><path d="M3 1 L5 3.5 L4 5 Q5.5 7 7 8 L8.5 7 L11 9 L9.5 11 Q5 10.5 1 3 Z" fill="var(--brand-red)"/></svg>
          <span>1-800-555-0142</span>
        </div>
        <div class="contact-line">
          <svg viewBox="0 0 12 12" aria-hidden="true"><rect x="1" y="2.5" width="10" height="7" fill="none" stroke="var(--brand-red)" stroke-width="1.4"/><path d="M1 2.5 L6 7 L11 2.5" fill="none" stroke="var(--brand-red)" stroke-width="1.4"/></svg>
          <span>dana@kestran.com</span>
        </div>
        <div class="contact-line">
          <svg viewBox="0 0 12 12" aria-hidden="true"><circle cx="6" cy="6" r="5" fill="none" stroke="var(--brand-red)" stroke-width="1.3"/><ellipse cx="6" cy="6" rx="2.2" ry="5" fill="none" stroke="var(--brand-red)" stroke-width="1"/><path d="M1 6 H11" stroke="var(--brand-red)" stroke-width="1"/></svg>
          <span>www.<span class="accent">kestran</span>.com</span>
        </div>
      </div>
    </div>
  </section>

</main>
</body>
</html>
```